Business Card for Web Design consulting firm

Business card designs for Web Design consulting firm

Target Market(s)

English speaking adults ages 30 - 60. Predominantly professional services eg. Doctor, Dentist

Industry/Entity Type

Consulting

Requirements
Must have
• Double sided card

```html
<!DOCTYPE html>
<html lang="en">
<head>
<meta charset="utf-8">
<title>Lumenta Business Card</title>
<link rel="stylesheet" href="https://fonts.googleapis.com/css2?family=Questrial&display=swap">
<style>
  :root {
    --orange: #f79c25;
    --charcoal: #4b4b4d;
    --paper: #ffffff;
    --edge: #d9d9d9;
  }
  * { margin: 0; padding: 0; box-sizing: border-box; }
  html, body {
    width: 1050px;
    height: 1200px;
    overflow: hidden;
    background: var(--paper);
  }
  body {
    position: relative;
    font-family: "Questrial", sans-serif;
    font-variant: small-caps;
    color: var(--charcoal);
  }
  .card {
    position: absolute;
    left: 25px;
    width: 1004px;
    height: 571px;
    box-shadow: 0 1px 4px rgba(0,0,0,0.25);
    border: 1px solid var(--edge);
    overflow: hidden;
  }
  .card-front { top: 17px; background: var(--paper); }
  .card-back { top: 624px; height: 564px; background: var(--orange); }

  .front-band {
    position: absolute;
    inset: 0;
    width: 100%;
    height: 100%;
  }
  .front-band polygon { fill: var(--orange); }

  .person {
    position: absolute;
    left: 32px;
    top: 20px;
    letter-spacing: 1px;
  }
  .person-name {
    font-size: 30px;
    color: var(--orange);
    line-height: 1.1;
  }
  .person-role {
    font-size: 30px;
    color: var(--charcoal);
    line-height: 1.1;
  }

  .contact {
    position: absolute;
    right: 26px;
    top: 24px;
    text-align: right;
    font-size: 23px;
    line-height: 25px;
    letter-spacing: 1.5px;
    color: var(--charcoal);
  }
  .contact-address { margin-bottom: 40px; }
  .contact-label { margin-right: 10px; }

  .brand {
    position: absolute;
    left: 30px;
    top: 270px;
    display: flex;
    align-items: center;
    gap: 28px;
  }
  .brand-dot {
    width: 70px;
    height: 70px;
    border-radius: 50%;
    background: var(--orange);
  }
  .brand-name {
    font-size: 96px;
    letter-spacing: 14px;
    color: var(--charcoal);
    line-height: 1;
    font-variant: normal;
  }
</style>
</head>
<body>
  <section class="card card-front">
    <svg class="front-band" viewBox="0 0 1004 571" preserveAspectRatio="none" aria-hidden="true">
      <polygon points="405,0 1004,0 1004,571 853,571"/>
    </svg>

    <div class="person">
      <p class="person-name">Mara Ellison</p>
      <p class="person-role">Sales Person</p>
    </div>

    <div class="contact">
      <div class="contact-address">
        <p>42 Sample Lane</p>
        <p>Hobart, 7000</p>
      </div>
      <p><span class="contact-label">P</span>07 5550 1234</p>
      <p><span class="contact-label">M</span>0400 555 012</p>
      <p><span class="contact-label">E</span>info@lumenta.com</p>
      <p><span class="contact-label">W</span>www.lumenta.com</p>
    </div>

    <div class="brand">
      <span class="brand-dot" aria-hidden="true"></span>
      <span class="brand-name">LUMENTA</span>
    </div>
  </section>

  <section class="card card-back" aria-label="Card back"></section>
</body>
</html>
```